Corvell Advisory

Business Development Consulting Firm

Target Market(s)

Federal Government, 8(a) companies, Small Businesses

Industry/Entity Type

Private Sector, US Government

Contact Information for Business Card

8(a) Program Capture, Business Development, Industry Trends & Analysis, Strategic Teaming, Cyber Solutions

Colors

Designer to choose colors to be used in the design.

```html
<!DOCTYPE html>
<html lang="en">
<head>
<meta charset="utf-8">
<title>Corvell Advisory — Business Cards</title>
<link href="https://fonts.googleapis.com/css2?family=Open+Sans:wght@400;700&display=swap" rel="stylesheet">
<style>
  :root {
    --backdrop: #232323;
    --card: #141414;
    --card-deep: #111111;
    --emboss: #1d1d1d;
    --gold: #dbb45e;
    --gold-light: #f0d27c;
    --gold-dark: #c99a4a;
    --ink-light: #f2f2f2;
  }
  * { box-sizing: border-box; margin: 0; padding: 0; }
  html, body {
    width: 1200px;
    height: 780px;
    overflow: hidden;
    background: var(--backdrop);
    font-family: "Open Sans", Arial, sans-serif;
  }
  .canvas {
    width: 1200px;
    height: 780px;
    display: flex;
    align-items: center;
    justify-content: center;
    gap: 40px;
  }
  .card {
    position: relative;
    width: 540px;
    height: 309px;
    background: var(--card);
    box-shadow: 0 14px 30px rgba(0, 0, 0, 0.45);
    overflow: hidden;
  }
  .card::before,
  .card::after {
    content: "";
    position: absolute;
    background: linear-gradient(90deg, var(--gold-dark), var(--gold-light), var(--gold));
  }
  .card::before { left: 0; top: 0; bottom: 0; width: 4px; background: linear-gradient(180deg, var(--gold-light), var(--gold-dark)); }
  .card::after { left: 0; right: 0; bottom: 0; height: 4px; }

  /* Front: embossed company name */
  .card--front { background: var(--card-deep); }
  .front-mark {
    position: absolute;
    inset: 0;
    display: flex;
    align-items: center;
    justify-content: center;
    gap: 16px;
  }
  .front-mark__dot {
    width: 26px;
    height: 26px;
    border-radius: 50%;
    background: var(--emboss);
  }
  .front-mark__name {
    font-weight: 700;
    font-size: 40px;
    letter-spacing: 2px;
    text-transform: uppercase;
    color: var(--emboss);
  }

  /* Back: name block + contacts */
  .brand {
    position: absolute;
    left: 40px;
    top: 0;
    bottom: 0;
    width: 230px;
    display: flex;
    align-items: center;
    gap: 10px;
  }
  .brand__dot {
    flex: none;
    width: 16px;
    height: 16px;
    border-radius: 50%;
    background: var(--gold);
  }
  .brand__name {
    font-weight: 700;
    font-size: 22px;
    line-height: 1.1;
    text-transform: uppercase;
    color: var(--gold);
  }
  .divider {
    position: absolute;
    left: 290px;
    top: 88px;
    height: 132px;
    width: 1px;
    background: var(--gold);
  }
  .contact {
    position: absolute;
    left: 310px;
    top: 74px;
    color: var(--ink-light);
  }
  .contact__name {
    font-weight: 700;
    font-size: 19px;
    color: var(--gold);
    text-transform: uppercase;
    line-height: 1.1;
  }
  .contact__role {
    font-size: 12px;
    margin-bottom: 12px;
  }
  .contact__list { list-style: none; }
  .contact__item {
    display: flex;
    align-items: center;
    gap: 6px;
    font-size: 12px;
    line-height: 1.55;
  }
  .contact__item svg { width: 11px; height: 11px; flex: none; }
  .contact__address {
    margin-top: 8px;
    margin-left: 17px;
    font-size: 12px;
    line-height: 1.35;
  }
</style>
</head>
<body>
<main class="canvas">
  <section class="card card--front" aria-label="Card front">
    <div class="front-mark">
      <span class="front-mark__dot"></span>
      <span class="front-mark__name">Corvell Advisory</span>
    </div>
  </section>

  <section class="card card--back" aria-label="Card back">
    <div class="brand">
      <span class="brand__dot"></span>
      <span class="brand__name">Corvell Advisory</span>
    </div>
    <div class="divider"></div>
    <div class="contact">
      <p class="contact__name">Marcus Hale</p>
      <p class="contact__role">Managing Director</p>
      <ul class="contact__list">
        <li class="contact__item">
          <svg viewBox="0 0 24 24" aria-hidden="true"><path fill="#dbb45e" d="M6.6 10.8a15.1 15.1 0 0 0 6.6 6.6l2.2-2.2c.3-.3.7-.4 1-.2 1.1.4 2.3.6 3.6.6.6 0 1 .4 1 1V20c0 .6-.4 1-1 1A17 17 0 0 1 3 4c0-.6.4-1 1-1h3.5c.6 0 1 .4 1 1 0 1.3.2 2.5.6 3.6.1.3 0 .7-.2 1z"/></svg>
          123 456 789
        </li>
        <li class="contact__item">
          <svg viewBox="0 0 24 24" aria-hidden="true"><path fill="#dbb45e" d="M3 5h18v14H3zm2 2v.4l7 4.6 7-4.6V7zm0 2.8V17h14V9.8l-7 4.6z"/></svg>
          info@corvelladvisory.com
        </li>
        <li class="contact__item">
          <svg viewBox="0 0 24 24" aria-hidden="true"><circle cx="12" cy="12" r="9" fill="none" stroke="#dbb45e" stroke-width="2"/><path d="M3 12h18M12 3c3 3 3 15 0 18M12 3c-3 3-3 15 0 18" fill="none" stroke="#dbb45e" stroke-width="1.6"/></svg>
          www.corvelladvisory.com
        </li>
      </ul>
      <p class="contact__address">Your address, City<br>State, Zip 1234</p>
    </div>
  </section>
</main>
</body>
</html>
```